Design Labels and Brand Look For Mens Soap Company

We are developing a mens soap line for a natural body wash and exfoliating bar. We will be selling this with our line of mens toiletry bags that we sell under the name of Kestrow Totes on Vendora. We are looking for you to design the product brand look with brand color palette and fonts.

The title for the mens body was is "Body Wash For Men". The title for the soap bar is "Exfoliating Bar Soap For Men"

We are providing the templates for these 2 items in PDF form. The final version of the design needs to be in a layered PSD format. You also need to send us the fonts used.

This soap will be sold on Vendora. Do a search for "men's body wash" and "mens soap bar" you will see our competition on page one. We need to stand out with colors and design differentiaon.

Target Market(s)

Men

Industry/Entity Type

Skin Care Product

Requirements
Must have
• Layered PSD file with all fonts

```html
<!DOCTYPE html>
<html lang="en">
<head>
<meta charset="UTF-8">
<title>Kestrow Body Wash For Men – Label</title>
<link rel="stylesheet" href="https://fonts.googleapis.com/css2?family=Cormorant+Garamond:wght@500;600&family=Arimo:wght@400&display=swap">
<style>
  :root {
    --navy: #170a55;
    --gold: #d4922e;
    --white: #ffffff;
    --trim-magenta: #b3247f;
    --safe-dash: #55557a;
    --page: #ffffff;
  }
  html, body {
    margin: 0;
    padding: 0;
    width: 1200px;
    height: 685px;
    overflow: hidden;
    background: var(--page);
  }
  .canvas {
    position: relative;
    width: 1200px;
    height: 685px;
  }
  .label {
    position: absolute;
    left: 38px;
    top: 42px;
    width: 1129px;
    height: 605px;
    background: var(--navy);
  }
  .label-guides {
    position: absolute;
    left: 0;
    top: 0;
    width: 1200px;
    height: 685px;
    pointer-events: none;
  }
  .vertical-copy {
    position: absolute;
    writing-mode: vertical-rl;
    font-family: "Arimo", Arial, sans-serif;
    color: var(--white);
  }
  .business-info {
    left: 78px;
    top: 90px;
    width: 74px;
    height: 510px;
    font-size: 15.5px;
    line-height: 24px;
    letter-spacing: 1.2px;
    text-align: center;
  }
  .usage-copy {
    left: 972px;
    top: 83px;
    width: 160px;
    height: 524px;
    transform: rotate(180deg);
    font-size: 14.6px;
    line-height: 19.5px;
    letter-spacing: 0.3px;
    text-align: justify;
    text-align-last: left;
  }
  .usage-copy p { margin: 0; }
  .usage-copy .directions { margin-left: 14px; }
  .brand-name {
    position: absolute;
    left: 0;
    width: 1200px;
    top: 172px;
    text-align: center;
    font-family: "Cormorant Garamond", Georgia, serif;
    font-weight: 600;
    font-size: 56px;
    line-height: 64px;
    color: var(--gold);
    margin: 0;
  }
  .product-title {
    position: absolute;
    left: 0;
    width: 1200px;
    top: 306px;
    margin: 0;
    text-align: center;
    font-family: "Cormorant Garamond", Georgia, serif;
    font-weight: 600;
    font-size: 58px;
    line-height: 51px;
    color: var(--white);
  }
  .product-title span { display: block; }
  .product-title .audience { color: var(--gold); font-size: 60px; }
  .product-variant {
    position: absolute;
    left: 0;
    width: 1200px;
    top: 505px;
    text-align: center;
    font-family: "Arimo", Arial, sans-serif;
    font-size: 22px;
    letter-spacing: 2px;
    color: var(--white);
    margin: 0;
  }
  .net-volume {
    position: absolute;
    left: 0;
    width: 1200px;
    top: 546px;
    text-align: center;
    font-family: "Arimo", Arial, sans-serif;
    font-size: 14.5px;
    letter-spacing: 2px;
    color: var(--white);
    margin: 0;
  }
</style>
</head>
<body>
<div class="canvas">
  <div class="label"></div>

  <svg class="label-guides" width="1200" height="685" viewBox="0 0 1200 685" aria-hidden="true">
    <rect x="58.5" y="63.5" width="1089" height="563" rx="6" fill="none" stroke="var(--safe-dash)" stroke-width="1" stroke-dasharray="8 6"/>
    <rect x="68.5" y="73.5" width="1068" height="543" fill="none" stroke="var(--trim-magenta)" stroke-width="1"/>
  </svg>

  <div class="vertical-copy business-info">
    [business name &amp; contact information<br>
    (incl. address with zip code &amp; telephone number)]<br>
    MADE IN USA
  </div>

  <p class="brand-name">Kestrow</p>

  <h1 class="product-title">
    <span>BODY</span>
    <span>WASH</span>
    <span class="audience">FOR MEN</span>
  </h1>

  <p class="product-variant">[product]</p>
  <p class="net-volume">16 FL OZ (473 mL)</p>

  <div class="vertical-copy usage-copy">
    <p class="directions">Pour a small amount of our luxurious hand soap into the palm of your hands and rub together under water for a rich, cleansing lather.</p>
    <p class="ingredients">Contains: Water, Sodium Laureth Sulfate, Vegetable Glycerine, ADDITIVES, Sodium Chloride, Fragrance, Citric Acid, Sodium Benzoate, Potassium Sorbate, Vitamin E, Cocoa Butter, Shea Butter, Virgin Olive Oil, Grapeseed Oil, COLORS.</p>
  </div>
</div>
</body>
</html>
```